Political Mail Out Quintero front and back

Front
Esteban (9th Grade) Quintero!

What's that famous saying?

Show me who your friends are and I'll tell you who you really are!
(show the two guys)

Walter Cuellar is charged with voter fraud by changing voter addresses from across the RGV so they could vote in Edinburg
Back
Did Esteban (9th Grade) Quintero commit voter fraud when he ran for office in 2016?
(insert blurred photo)

Here is a list of people from all over the RGV that voted in Edinburg in the 2016 race.
Here is a break down:

(highlight the number and where they were first registered to vote)

9 People voted in Edinburg who were registered in Donna.
13 People voted in Edinburg who were registered in San Juan
8 People voted in Edinburg who were registered in Pharr
31 People voted in Edinburg who were registered in McAllen
2 People voted in Edinburg who were registered in La Joya
6 People voted in Edinburg who were registered in Edcouch
2 People voted in Edinburg who were registered in Mercedes
2 People voted in Edinburg who were registered in Monte Alto
6 People voted in Edinburg who were registered in Weslaco
1 Person voted in Edinburg who were registered in Penitas
3 People voted in Edinburg who were registered in Alamo
5 People voted in Edinburg who were registered in Elsa
6 People voted in Edinburg who were registered in Mission
1 Person voted in Edinburg who were registered in Alton

Will Esteban (9th Grade) Quintero CHEAT in 2020?

Only time will tell.

Vote Esteban (9th Grade) Quintero OUT of office.

```html
<!DOCTYPE html>
<html lang="en">
<head>
<meta charset="utf-8">
<title>Vote Esteban (9th Grade) Quintero Out of Office</title>
<link href="https://fonts.googleapis.com/css2?family=Roboto+Condensed:wght@400;700&display=swap" rel="stylesheet">
<style>
  :root {
    --blue: #1c05f2;
    --red: #fa0505;
    --white: #ffffff;
    --yellow: #ffff00;
    --sheet-light: #dcddd9;
    --sheet-mid: #c4c6c1;
    --sheet-dark: #9fa29c;
  }
  * { margin: 0; padding: 0; box-sizing: border-box; }
  html, body { width: 800px; height: 1200px; overflow: hidden; background: var(--white); }
  body { font-family: "Roboto Condensed", "Arial Narrow", sans-serif; color: var(--white); }
  .mailer { position: relative; width: 800px; height: 1200px; background: var(--white); }

  .headline-band {
    position: absolute; left: 0; top: 0; width: 800px; height: 229px;
    background: var(--blue);
  }
  .headline {
    position: absolute; left: 55px; top: 16px;
    font-size: 56px; line-height: 67px; font-weight: 400; white-space: nowrap;
    letter-spacing: -0.3px;
  }
  .headline b { font-weight: 700; }
  .star { position: absolute; left: 662px; top: 104px; width: 84px; height: 80px; }

  .evidence-photo {
    position: absolute; left: 0; top: 240px; width: 372px; height: 677px;
    background: linear-gradient(90deg,
      var(--sheet-light) 0%, var(--sheet-light) 60%,
      var(--sheet-mid) 66%, var(--sheet-dark) 82%, var(--sheet-mid) 100%);
  }

  .intro-box {
    position: absolute; left: 372px; top: 240px; width: 428px; height: 124px;
    background: var(--red);
    display: flex; align-items: center; justify-content: center;
    text-align: center; font-weight: 700; font-size: 27px; line-height: 31px;
  }

  .breakdown {
    position: absolute; left: 372px; top: 364px; width: 428px; height: 553px;
    background: var(--blue);
  }
  .breakdown-title {
    position: absolute; left: 0; top: 14px; width: 100%;
    text-align: center; font-weight: 700; font-size: 27px;
  }
  .breakdown-list {
    position: absolute; left: 23px; top: 64px; list-style: none;
    font-size: 16px; line-height: 33.3px; white-space: nowrap;
  }
  .breakdown-list .count, .breakdown-list .town { color: var(--yellow); font-weight: 700; }

  .closing-band {
    position: absolute; left: 0; top: 926px; width: 800px; height: 274px;
    background: var(--red);
  }
  .closing {
    position: absolute; left: 35px; font-size: 36px; white-space: nowrap; line-height: 1;
  }
  .closing b { font-weight: 700; }
  .closing.question { top: 44px; }
  .closing.wait { top: 92px; font-weight: 700; }
  .closing.call { top: 184px; font-size: 38px; font-weight: 700; }
</style>
</head>
<body>
<main class="mailer">
  <header class="headline-band">
    <h1 class="headline"><b>Did Esteban</b> (9th Grade) <b>Quintero</b><br><b>commit voter fraud</b> when<br>he ran for office in <b>2016?</b></h1>
    <svg class="star" viewBox="0 0 100 95" aria-hidden="true">
      <polygon points="50,0 61.8,36.3 100,36.3 69.1,58.8 80.9,95 50,72.6 19.1,95 30.9,58.8 0,36.3 38.2,36.3" fill="var(--white)"/>
    </svg>
  </header>

  <div class="evidence-photo" role="img" aria-label="Blurred photo of a spreadsheet listing voter addresses from towns across the RGV"></div>

  <section class="intro-box">
    <p>Here is a list of people from all<br>over the RGV that voted in<br>Edinburg in the 2016 race.</p>
  </section>

  <section class="breakdown">
    <h2 class="breakdown-title">Here is a break down:</h2>
    <ul class="breakdown-list">
      <li><span class="count">9</span> People voted in Edinburg who were registered in <span class="town">Donna</span></li>
      <li><span class="count">13</span> People voted in Edinburg who were registered in <span class="town">San Juan</span></li>
      <li><span class="count">8</span> People voted in Edinburg who were registered in <span class="town">Pharr</span></li>
      <li><span class="count">31</span> People voted in Edinburg who were registered in <span class="town">McAllen</span></li>
      <li><span class="count">2</span> People voted in Edinburg who were registered in <span class="town">La Joya</span></li>
      <li><span class="count">6</span> People voted in Edinburg who were registered in <span class="town">Edcouch</span></li>
      <li><span class="count">2</span> People voted in Edinburg who were registered in <span class="town">Mercedes</span></li>
      <li><span class="count">2</span> People voted in Edinburg who were registered in <span class="town">Monte Alto</span></li>
      <li><span class="count">6</span> People voted in Edinburg who were registered in <span class="town">Weslaco</span></li>
      <li><span class="count">1</span> Person voted in Edinburg who were registered in <span class="town">Penitas</span></li>
      <li><span class="count">3</span> People voted in Edinburg who were registered in <span class="town">Alamo</span></li>
      <li><span class="count">5</span> People voted in Edinburg who were registered in <span class="town">Elsa</span></li>
      <li><span class="count">6</span> People voted in Edinburg who were registered in <span class="town">Mission</span></li>
      <li><span class="count">1</span> Person voted in Edinburg who were registered in <span class="town">Alton</span></li>
    </ul>
  </section>

  <footer class="closing-band">
    <p class="closing question">Will <b>Esteban</b> (9th Grade) <b>Quintero CHEAT</b> in 2020?</p>
    <p class="closing wait">Only time will tell.</p>
    <p class="closing call">Vote Esteban (9th Grade) Quintero OUT of office!</p>
  </footer>
</main>
</body>
</html>
```